Folder and Swag Design for Law Firm

We are a personal injury law firm designing new client materials for folders and other swag that will go to clients once they retain us. Rather than just being white on green, or green on white, we'd like a design to put on the items. One idea that we had was a wave that included our slogan of "Our family protecting yours" that can wrap around a folder, or a tumbler but we are open to other ideas. I've attached a sketch of the wave design and our logo.
The final design should communicate a family protective feel.
Branding colors: #FFFFFF, #0FA57B, #00CA88
Victims of personal injury (car accidents, slip and falls, defective products).
Legal Services

```html
<!DOCTYPE html>
<html lang="en">
<head>
<meta charset="utf-8">
<title>Harlow &amp; Brandt — Client Folder</title>
<link rel="stylesheet" href="https://fonts.googleapis.com/css2?family=Playfair+Display:ital,wght@1,600;1,700&family=Poppins:wght@400;600&family=Cinzel:wght@400&display=swap">
<style>
  :root {
    --bg: #8a8a8a;
    --green: #3aa57a;
    --green-deep: #1f8a60;
    --green-soft: #7fc5a8;
    --ink: #1b343a;
    --white: #ffffff;
    --band: #f1f1f1;
  }
  * { margin: 0; padding: 0; box-sizing: border-box; }
  html, body { width: 1200px; height: 960px; overflow: hidden; background: var(--bg); }
  .folder { position: relative; width: 1200px; height: 960px; }
  .folder-art { position: absolute; inset: 0; }
  .copy { position: absolute; color: var(--white); font-family: "Poppins", sans-serif; }
  .reviews-title { left: 284px; top: 158px; font-size: 17px; font-weight: 600; }
  .reviews-rule { position: absolute; left: 284px; top: 189px; width: 323px; height: 1.5px; background: var(--white); }
  .highlights { left: 284px; top: 201px; list-style: none; font-size: 9.6px; line-height: 19px; }
  .highlights li { display: flex; align-items: center; gap: 6px; }
  .highlights svg { width: 9px; height: 9px; }
  .experience { left: 285px; top: 305px; font-family: "Playfair Display", serif; font-style: italic; font-weight: 700; font-size: 17.5px; line-height: 24px; }
  .phone { left: 384px; top: 661px; font-size: 9.6px; display: flex; align-items: center; gap: 5px; }
  .address { right: 587px; top: 647px; font-size: 9.6px; line-height: 12px; text-align: right; }
  .address span { display: inline-block; width: 8px; }
  .firm { left: 742px; top: 558px; display: flex; align-items: center; gap: 12px; }
  .firm-square { width: 52px; height: 52px; background: var(--white); }
  .firm-name { font-family: "Cinzel", serif; font-size: 16px; letter-spacing: 0.5px; color: var(--white); }
  .website { left: 743px; top: 643px; font-size: 10px; font-weight: 600; letter-spacing: 3.6px; }
  .slogan { font-family: "Playfair Display", serif; font-style: italic; font-weight: 700; fill: var(--green); }
</style>
</head>
<body>
<div class="folder">
  <svg class="folder-art" viewBox="0 0 1200 960" width="1200" height="960">
    <defs>
      <linearGradient id="field" x1="0" y1="0" x2="0" y2="1">
        <stop offset="0" stop-color="#fbf3e4"/>
        <stop offset="0.45" stop-color="#d9b27a"/>
        <stop offset="1" stop-color="#8a5a2a"/>
      </linearGradient>
      <linearGradient id="sheen" x1="0" y1="0" x2="1" y2="0">
        <stop offset="0" stop-color="#ffffff"/>
        <stop offset="0.5" stop-color="#e4e4e4"/>
        <stop offset="0.75" stop-color="#ffffff"/>
        <stop offset="1" stop-color="#eeeeee"/>
      </linearGradient>
      <path id="slogan-line" d="M272,582 C470,540 560,510 700,470 S950,385 1050,356"/>
    </defs>

    <!-- spine and flaps -->
    <rect class="spine" x="80" y="111" width="160" height="587" fill="var(--ink)"/>
    <polygon class="pocket-flap" points="239,698 654,698 627,849 239,849" fill="var(--ink)"/>
    <polygon class="side-flap" points="1081,521 1119,533 1119,686 1081,698" fill="var(--ink)"/>
    <g class="card-slits" stroke="var(--white)" stroke-width="1.2">
      <line x1="359" y1="759" x2="384" y2="734"/>
      <line x1="509" y1="734" x2="534" y2="759"/>
      <line x1="359" y1="788" x2="384" y2="813"/>
      <line x1="509" y1="813" x2="534" y2="788"/>
    </g>

    <!-- front panels -->
    <rect class="panel" x="239" y="111" width="842" height="587" fill="var(--green)"/>
    <rect role="img" aria-label="Photo of a happy family running through a sunlit meadow" x="666" y="111" width="415" height="230" fill="url(#field)"/>

    <!-- wave accents -->
    <path d="M239,436 C280,470 300,460 336,447 C380,430 420,440 470,420 C520,402 540,400 560,410 L560,470 L239,520 Z" fill="var(--green-soft)" opacity="0.8"/>
    <path d="M666,340 C700,310 730,300 780,330 C820,300 850,290 900,305 C960,290 1030,262 1081,272 L1081,290 C1020,290 960,320 900,320 C850,320 820,330 780,345 Z" fill="var(--green-deep)"/>
    <path d="M300,460 C340,440 380,440 410,452 C440,432 480,422 520,440 L520,452 C480,442 440,450 410,464 C380,452 340,452 300,470 Z" fill="var(--green-deep)"/>
    <path d="M520,600 C620,580 700,545 780,505 C840,495 900,470 960,465 C1010,455 1050,445 1081,438 L1081,450 C1030,470 980,480 940,485 C860,500 790,540 720,560 C640,600 580,615 520,615 Z" fill="var(--green-soft)" opacity="0.85"/>
    <path d="M239,624 C270,640 300,656 340,645 C400,628 440,630 470,620 C560,600 620,585 680,560 C740,530 770,500 810,480 C880,470 960,456 1081,438 L1081,446 C960,470 890,480 820,492 C770,520 740,548 690,572 C620,600 560,612 470,630 C430,642 390,640 340,656 C300,668 270,655 239,640 Z" fill="var(--green-deep)"/>

    <!-- white slogan band -->
    <path class="slogan-band" d="M239,474 C280,460 300,447 336,447 C380,447 400,428 444,429 C520,430 600,370 666,324 C690,310 705,308 720,312 C745,318 760,336 780,336 C805,336 825,300 852,300 C885,300 905,312 936,309 C990,304 1040,270 1081,270 L1081,441 C1040,450 990,456 960,456 C920,460 900,495 864,495 C830,495 810,488 780,492 C740,505 720,534 660,560 C600,580 560,594 540,594 C500,606 480,620 456,618 C400,615 330,648 294,642 C270,638 255,630 239,624 Z" fill="url(#sheen)"/>
    <line x1="666" y1="322" x2="666" y2="570" stroke="#d8d8d8" stroke-width="1"/>

    <text class="slogan" font-size="58" fill="#1b7f58" opacity="0.35" transform="translate(2,2)"><textPath href="#slogan-line" textLength="780" lengthAdjust="spacing">Our Family Fighting for Yours</textPath></text>
    <text class="slogan" font-size="58"><textPath href="#slogan-line" textLength="780" lengthAdjust="spacing">Our Family Fighting for Yours</textPath></text>
  </svg>

  <h2 class="copy reviews-title">Over 300 Client Reviews</h2>
  <div class="reviews-rule"></div>
  <ul class="copy highlights">
    <li><svg viewBox="0 0 10 10"><circle cx="5" cy="5" r="4.3" fill="none" stroke="#fff" stroke-width="0.9"/><path d="M3,5.2 L4.5,6.6 L7.2,3.6" fill="none" stroke="#fff" stroke-width="0.9"/></svg>Top-Rated Fort Myers Personal Injury Lawyers.</li>
    <li><svg viewBox="0 0 10 10"><circle cx="5" cy="5" r="4.3" fill="none" stroke="#fff" stroke-width="0.9"/><path d="M3,5.2 L4.5,6.6 L7.2,3.6" fill="none" stroke="#fff" stroke-width="0.9"/></svg>We Won over $100,000,000 in Verdicts and Settlements.</li>
    <li><svg viewBox="0 0 10 10"><circle cx="5" cy="5" r="4.3" fill="none" stroke="#fff" stroke-width="0.9"/><path d="M3,5.2 L4.5,6.6 L7.2,3.6" fill="none" stroke="#fff" stroke-width="0.9"/></svg>Proudly Serving Florida for 40+ Years.</li>
    <li><svg viewBox="0 0 10 10"><circle cx="5" cy="5" r="4.3" fill="none" stroke="#fff" stroke-width="0.9"/><path d="M3,5.2 L4.5,6.6 L7.2,3.6" fill="none" stroke="#fff" stroke-width="0.9"/></svg>Call or text for FREE Consultation. Habla Español.</li>
  </ul>
  <p class="copy experience">Over 40 Years of Combined<br>Personal Injury Experience in Florida</p>

  <p class="copy phone"><svg width="10" height="10" viewBox="0 0 10 10"><circle cx="5" cy="5" r="4.4" fill="none" stroke="#fff" stroke-width="0.8"/><path d="M3.4,2.8 L4.2,2.6 L4.6,3.9 L4,4.3 C4.3,5 4.9,5.7 5.7,6 L6.1,5.4 L7.3,5.8 L7.1,6.6 C5.2,6.8 3.3,4.9 3.4,2.8 Z" fill="#fff"/></svg>(555) 014-2290</p>
  <p class="copy address"><svg width="7" height="9" viewBox="0 0 7 9"><circle cx="3.5" cy="3" r="2.3" fill="none" stroke="#fff" stroke-width="0.9"/><line x1="3.5" y1="5.3" x2="3.5" y2="8.5" stroke="#fff" stroke-width="0.9"/></svg> 1820 Harbor Point Court<br>Fort Myers, FL 33900</p>

  <div class="copy firm">
    <div class="firm-square"></div>
    <span class="firm-name">HARLOW &amp; BRANDT, LLC</span>
  </div>
  <p class="copy website">WWW.HARLOWANDBRANDT.COM</p>
</div>
</body>
</html>
```